Horse Brush Package design -

I need a design for a box - required for a rubber horse brush used for grooming and removing excess hair. The Brand is 'Fable Ridge Equestrian' and we develop top quality horse products. The design should be classy and professional

Box size is 21.5cm Length * 2cm high * 5 cm wide
Photo of logo and brush attached.
Box needs to have logo and description on front
Barcode on back.
Additional designs and photos can be added as you see fit.

"Horse Deshedding & Grooming Brush"
Brush away excess coat and dander
Gently remove dirt and mud
Soft, flexible design to gently groom around legs, ears and face.
Used when washing gives a deep clean to remove dirt
Gentle massage for increasing circulation
Durable, gentle, and kind to the horse

Target Market(s)

Horse Owners

Requirements
Must have
• Logo on the front, space for barcode on the back
Nice to have
• A nice horse photo would be suitable

```html
<!DOCTYPE html>
<html lang="en">
<head>
<meta charset="utf-8">
<title>Fable Ridge Equestrian – Brush Box Dieline</title>
<link href="https://fonts.googleapis.com/css2?family=Poppins:wght@400;500;600&display=swap" rel="stylesheet">
<style>
  :root {
    --page: #ffffff;
    --board: #1e1e1c;
    --fold: #1a9a4a;
    --ink: #ffffff;
    --ink-soft: #d9d9d9;
    --ghost-a: rgba(255,255,255,0.07);
    --ghost-b: rgba(255,255,255,0);
  }
  * { box-sizing: border-box; margin: 0; padding: 0; }
  html, body { width: 1200px; height: 1200px; overflow: hidden; background: var(--page); }
  body { position: relative; font-family: "Poppins", Arial, sans-serif; color: var(--ink); }

  .panel {
    position: absolute;
    background: var(--board);
    border: 1px solid var(--fold);
    overflow: hidden;
    display: flex;
    align-items: center;
    justify-content: center;
  }
  .panel--top-flap   { left: 190px; top: 330px; width: 827px; height: 78px; }
  .panel--front      { left: 190px; top: 407px; width: 827px; height: 194px; flex-direction: column; }
  .panel--side-left  { left: 113px; top: 407px; width: 78px; height: 194px; border-right: none; }
  .panel--side-right { left: 1016px; top: 407px; width: 78px; height: 194px; border-left: none; }
  .panel--bottom     { left: 190px; top: 600px; width: 827px; height: 78px; }
  .panel--back       { left: 190px; top: 677px; width: 827px; height: 193px; }

  .brand-name {
    font-family: "Poppins", Arial, sans-serif;
    font-weight: 500;
    color: var(--ink);
    text-transform: uppercase;
    letter-spacing: 0.06em;
    white-space: nowrap;
    display: flex;
    align-items: center;
    gap: 10px;
  }
  .brand-name__mark {
    width: 9px; height: 9px;
    border: 1px solid var(--ink);
    border-radius: 50%;
  }
  .brand-name--small { font-size: 13px; }
  .brand-name--large { font-size: 24px; gap: 14px; }
  .brand-name--large .brand-name__mark { width: 14px; height: 14px; }
  .brand-name--flipped { transform: rotate(180deg); }
  .brand-name--side { font-size: 11px; }
  .brand-name--down { transform: rotate(90deg); }
  .brand-name--up { transform: rotate(-90deg); }

  .front-ghost {
    position: absolute;
    left: 0; top: 30px;
    width: 115px; height: 164px;
    background: radial-gradient(ellipse at 55% 45%, var(--ghost-a), var(--ghost-b) 70%);
  }

  .product-title {
    margin-top: 22px;
    font-size: 17px;
    font-weight: 600;
    letter-spacing: -0.01em;
  }
  .product-copy {
    margin-top: 14px;
    font-size: 5.6px;
    line-height: 1.35;
    text-align: center;
    color: var(--ink-soft);
  }

  .feature {
    position: absolute;
    right: 22px; top: 148px;
    display: flex; flex-direction: column; align-items: center; gap: 3px;
  }
  .feature__label { font-size: 4.5px; font-weight: 600; }
</style>
</head>
<body>

  <section class="panel panel--top-flap" aria-label="Top flap">
    <div class="brand-name brand-name--small brand-name--flipped"><span class="brand-name__mark"></span>Fable Ridge Equestrian</div>
  </section>

  <section class="panel panel--side-left" aria-label="Left end">
    <div class="brand-name brand-name--side brand-name--down">Fable Ridge Equestrian</div>
  </section>

  <section class="panel panel--front" aria-label="Front panel">
    <div class="front-ghost" role="img" aria-label="Faint horse head illustration"></div>
    <div class="brand-name brand-name--large"><span class="brand-name__mark"></span>Fable Ridge Equestrian</div>
    <h1 class="product-title">"Horse Deshedding &amp; Grooming Brush"</h1>
    <p class="product-copy">
      Brush away excess coat and dander. Gently remove dirt and mud. Soft, flexible design to gently groom around legs, ears and face.<br>
      Used when washing gives a deep clean to remove dirt. Gentle massage for increasing circulation.<br>
      Durable, gentle, and kind to the horse
    </p>
    <div class="feature">
      <svg class="feature__icon" width="34" height="20" viewBox="0 0 34 20" aria-hidden="true">
        <rect x="1" y="1" width="32" height="18" rx="3" fill="none" stroke="#fff" stroke-width="1.4"/>
        <rect x="4" y="4" width="26" height="12" rx="1.5" fill="none" stroke="#fff" stroke-width="0.8"/>
        <g fill="#fff">
          <rect x="6" y="6" width="22" height="1.2"/>
          <rect x="6" y="9.4" width="22" height="1.2"/>
          <rect x="6" y="12.8" width="22" height="1.2"/>
        </g>
      </svg>
      <span class="feature__label">multi-point design</span>
    </div>
  </section>

  <section class="panel panel--side-right" aria-label="Right end">
    <div class="brand-name brand-name--side brand-name--up">Fable Ridge Equestrian</div>
  </section>

  <section class="panel panel--bottom" aria-label="Base panel">
    <div class="brand-name brand-name--small"><span class="brand-name__mark"></span>Fable Ridge Equestrian</div>
  </section>

  <section class="panel panel--back" aria-label="Back panel"></section>

</body>
</html>
```